construction co.logo(ie.highway,heavy equip)

need a design for a new construction company in washington state,office is located on the water (beach front)also use a 1952 dunmore keel avalis as portable office,or the standard bold construction type logo's,these are just thoughts and not necassarily direction

Target Market(s)

I will be working as a sub to much larger general contractors and am looking for a strong,stable appearance.

Industry/Entity Type

Construction

```html
<!DOCTYPE html>
<html lang="en">
<head>
<meta charset="utf-8">
<title>Tideline Build — Business Cards</title>
<link rel="stylesheet" href="https://fonts.googleapis.com/css2?family=Jost:wght@400;500;600&display=swap">
<style>
  :root {
    --canvas: #e9e6e1;
    --card-dark: #2e2e2f;
    --card-edge: #1c1c1c;
    --safety-yellow: #f5cf0f;
    --band-deep: #1a1a1a;
    --steel-light: #d9dadc;
    --steel-mid: #a9abae;
    --steel-dark: #8c8e91;
    --text-light: #f4f4f4;
    --text-dim: #cfcfcf;
    --text-ink: #2b2b2b;
  }
  * { box-sizing: border-box; margin: 0; padding: 0; }
  html, body {
    width: 1200px; height: 900px; overflow: hidden;
    background: var(--canvas);
    font-family: "Jost", "Futura", sans-serif;
  }
  .sheet {
    width: 1200px; height: 900px;
    display: flex; flex-direction: column;
    align-items: center; justify-content: center; gap: 40px;
  }
  .card {
    position: relative; width: 640px; height: 360px;
    background: var(--card-dark);
    overflow: hidden;
    box-shadow: 0 10px 24px rgba(0,0,0,.25);
  }
  .accent-band {
    position: absolute; left: 0; right: 0; height: 16px;
    background: linear-gradient(90deg, var(--band-deep) 0%, #6b5a10 50%, var(--band-deep) 100%);
    border-top: 3px solid var(--safety-yellow);
  }

  /* Contact card */
  .contact-card .brand {
    position: absolute; left: 42px; top: 52px;
    display: flex; align-items: center; gap: 14px;
  }
  .brand-ring {
    width: 50px; height: 50px; border-radius: 50%;
    background: var(--card-edge);
    border: 5px solid var(--safety-yellow);
  }
  .brand-name {
    color: var(--text-light); font-weight: 500; font-size: 26px; letter-spacing: .2px;
  }
  .person {
    position: absolute; right: 36px; top: 44px;
    display: flex; align-items: center; gap: 12px;
    color: var(--text-dim); font-size: 15px; letter-spacing: .6px;
  }
  .person-name { text-transform: uppercase; }
  .person-divider { width: 2px; height: 24px; background: var(--safety-yellow); }
  .contact-card .accent-band { top: 150px; }
  .steel-band {
    position: absolute; left: 0; right: 0; top: 166px; bottom: 0;
    background: linear-gradient(100deg, var(--steel-dark) 0%, var(--steel-mid) 30%,
      var(--steel-light) 55%, var(--steel-mid) 80%, var(--steel-dark) 100%);
  }
  .details {
    position: absolute; left: 400px; top: 24px;
    list-style: none; color: var(--text-ink); font-size: 14px; line-height: 22px;
  }
  .details .address { margin-bottom: 2px; }
  .details .bullet { display: flex; align-items: center; gap: 8px; }
  .details .bullet::before {
    content: ""; width: 5px; height: 11px; background: var(--safety-yellow);
  }

  /* Brand card */
  .brand-card .brand-stack {
    position: absolute; left: 0; right: 0; top: 96px;
    display: flex; flex-direction: column; align-items: center; gap: 12px;
  }
  .brand-card .brand-ring { width: 80px; height: 80px; border-width: 7px; }
  .brand-card .brand-name { font-size: 34px; }
  .brand-card .accent-band.top { top: 0; border-top: 0; border-bottom: 3px solid var(--safety-yellow); }
  .brand-card .accent-band.bottom { bottom: 0; }
</style>
</head>
<body>
<main class="sheet">
  <section class="card contact-card">
    <div class="brand">
      <span class="brand-ring"></span>
      <span class="brand-name">Tideline Build</span>
    </div>
    <div class="person">
      <span class="person-name">Mara Okonkwo</span>
      <span class="person-divider"></span>
      <span class="person-title">Company Director</span>
    </div>
    <div class="accent-band" role="img" aria-label="Yellow and black safety stripe band"></div>
    <div class="steel-band">
      <ul class="details">
        <li class="address">1187 Harbor Bend #40</li>
        <li class="address">Port Selwyn, TM 041172</li>
        <li class="bullet">hello@tidelinebuild.com</li>
        <li class="bullet">555 014 2280</li>
        <li class="bullet">555 014 2281</li>
      </ul>
    </div>
  </section>

  <section class="card brand-card">
    <div class="accent-band top" role="img" aria-label="Yellow and black safety stripe band"></div>
    <div class="brand-stack">
      <span class="brand-ring"></span>
      <span class="brand-name">Tideline Build</span>
    </div>
    <div class="accent-band bottom" role="img" aria-label="Yellow and black safety stripe band"></div>
  </section>
</main>
</body>
</html>
```